Design cd cover for the vocal group: Ember, cd title Harbor Light. Cd cover is for EP release to be followed by full album. Songs are: Silela Nkwe Dumo(Carry the lantern); Under Cedar; Sikhanda(Over the quiet river); When Dawn Came. There is no track entitled harbor light; the concept of the sound of gospel music as embodied in the music tracks - contemporary and traditional - is the basis of the album title.
NB: Project can close Tuesday 12 November to account for the 5 days as I do not count Saturday as a working day.
Hey guys,
Hello to everyone. I would like to take this opportunity to say thank you for your participation. Your submissions have been great and much appreciated. Forgive me for not being able to provide feedback to all of you. The time has come for me to make selection decisions and I would like to say thank you to all for your participation, you have been great and amazing.

```html
<!DOCTYPE html>
<html lang="en">
<head>
<meta charset="utf-8">
<title>Ember — Harbor Light EP Cover</title>
<link rel="stylesheet" href="https://fonts.googleapis.com/css2?family=Mrs+Saint+Delafield&family=Oswald:wght@500&display=swap">
<style>
  :root {
    --frame: #0f0e0d;
    --sky-top: #34383a;
    --sky-upper: #4b4c45;
    --sky-gold: #c9a55a;
    --sky-glow: #e9cf8a;
    --sky-amber: #cf7a2c;
    --sky-ember: #c2501a;
    --land: #17130f;
    --ink: rgba(38, 33, 26, 0.88);
  }
  html, body {
    margin: 0;
    padding: 0;
    width: 1200px;
    height: 1200px;
    overflow: hidden;
    background: var(--frame);
  }
  .cover {
    position: relative;
    width: 1200px;
    height: 1200px;
    background: var(--frame);
    overflow: hidden;
  }
  .cover__sky {
    position: absolute;
    left: 17px;
    top: 17px;
    right: 17px;
    bottom: 17px;
    background:
      radial-gradient(ellipse 70% 45% at 35% 62%, rgba(240, 214, 150, 0.55), transparent 70%),
      radial-gradient(ellipse 120% 90% at 50% 50%, transparent 55%, rgba(10, 9, 8, 0.55) 100%),
      linear-gradient(180deg,
        var(--sky-top) 0%,
        var(--sky-upper) 22%,
        var(--sky-gold) 45%,
        var(--sky-glow) 58%,
        var(--sky-amber) 74%,
        var(--sky-ember) 84%,
        #5a2a12 90%,
        var(--land) 96%);
  }
  .cover__band {
    position: absolute;
    left: 0;
    width: 100%;
    background: var(--ink);
    height: 2px;
    top: 693px;
  }
  .brand {
    position: absolute;
    left: 0;
    width: 100%;
    top: 362px;
    text-align: center;
    font-family: "Oswald", sans-serif;
    font-weight: 500;
    font-size: 46px;
    letter-spacing: 6px;
    color: var(--ink);
    text-transform: uppercase;
  }
  .title {
    position: absolute;
    left: 0;
    top: 0;
    width: 1200px;
    height: 1200px;
  }
  .title__script {
    position: absolute;
    left: 300px;
    width: 600px;
    top: 420px;
    text-align: center;
    font-family: "Mrs Saint Delafield", cursive;
    font-size: 300px;
    line-height: 1;
    color: var(--ink);
  }
  .title__rule {
    position: absolute;
    top: 693px;
    height: 2px;
    background: var(--ink);
  }
  .title__rule--a { left: 326px; width: 131px; }
  .title__rule--b { left: 498px; width: 112px; }
  .title__rule--c { left: 758px; width: 114px; }
  .title__sub {
    position: absolute;
    left: 614px;
    width: 140px;
    top: 672px;
    text-align: center;
    font-family: "Oswald", sans-serif;
    font-weight: 500;
    font-size: 38px;
    line-height: 44px;
    color: var(--ink);
    text-transform: uppercase;
  }
</style>
</head>
<body>
  <main class="cover">
    <div class="cover__sky" role="img" aria-label="Photograph of a sunset sky with dark clouds over a golden and orange horizon above a silhouetted tree line"></div>
    <div class="brand">Ember</div>
    <div class="title">
      <div class="title__script">Harbor</div>
      <span class="title__rule title__rule--a"></span>
      <span class="title__rule title__rule--b"></span>
      <div class="title__sub">Light</div>
      <span class="title__rule title__rule--c"></span>
    </div>
  </main>
</body>
</html>
```